Business Cards and Logo

KMR - Personal Injury Attorneys is the name of the firm.
We are personal injury lawyers. We want a crisp, modern and impactful design.
Color schemes are white, matte black and light grey OR white, matte black and red OR white, matte black and a nice blue or yellow.
For logo - we don’t want typical logos like scales of justice or a hammer. We want a general design with the KMR letters.
Target Market(s)
People who need attorneys.
Industry/Entity Type
Law Firm
Contact Information for Business Card
Back side: text: Los Angeles - Santa Ana - San Diego - San Francisco
Front side
Name of firm and logo.
Tomas Velquist
712 W. Harlow Ave. 4th Floor
Brookvale, CA 90000
(555)014-2736 (c)
(555)019-6521 (o)
Tomas@counselwestex.com
Logo Text
KMR
Font styles to use
Other font styles liked:
- Musk - regular. Military - regular. Moonglade. Future. Or similar fonts.
Requirements
Must have
- See above. Nothing else to provide.
- KMR - Personal Injury Attorneys is the name of the firm.
- We are personal injury lawyers. We want a crisp, modern and impactful design.
- Color schemes are white, matte black and light grey OR white, matte black and red OR white, matte black and a nice blue or yellow.
- For logo - we don’t want typical logos like scales of justice or a hammer. We want a general design with the KMR letters.
Nice to have
- See above - nothing else to provide.
Should not have

```html
<!DOCTYPE html>
<html lang="en">
<head>
<meta charset="utf-8">
<title>KMR - Personal Injury Attorneys — Business Card</title>
<link rel="stylesheet" href="https://fonts.googleapis.com/css2?family=Cinzel:wght@400;500&family=Lato:wght@400;700&family=Roboto+Condensed:wght@500&display=swap">
<style>
  :root {
    --backdrop: #2a2a2b;
    --card-black: #1e1f21;
    --pattern-tone: #262729;
    --white: #f2f2f2;
    --grey-line: #6a6a6c;
    --red: #d0123f;
  }
  * { margin: 0; padding: 0; box-sizing: border-box; }
  html, body {
    width: 1200px; height: 1108px; overflow: hidden;
    background: var(--backdrop);
  }
  .stage {
    position: relative; width: 1200px; height: 1108px;
    display: flex; justify-content: center; align-items: center; gap: 80px;
  }
  .card {
    position: relative; width: 400px; height: 680px;
    background: var(--card-black); border-radius: 24px; overflow: hidden;
    color: var(--white); text-align: center;
  }
  /* Front */
  .front__mark {
    margin-top: 96px;
    font-family: "Lato", sans-serif; font-weight: 400;
    font-size: 118px; letter-spacing: 4px; line-height: 1;
    color: var(--white);
  }
  .front__firm {
    margin-top: 18px;
    font-family: "Cinzel", serif; font-weight: 400;
    font-size: 29px; line-height: 1.05; letter-spacing: 1px;
  }
  .front__name {
    margin-top: 56px;
    font-family: "Cinzel", serif; font-weight: 500;
    font-size: 27px; letter-spacing: 1px; color: var(--red);
  }
  .divider {
    display: flex; align-items: center; justify-content: center;
    gap: 8px; margin: 18px 40px 0;
  }
  .divider__rule { flex: 1; height: 1px; background: var(--grey-line); }
  .divider__icon {
    width: 26px; height: 26px; border-radius: 50%; background: var(--red);
    display: flex; align-items: center; justify-content: center;
  }
  .contact {
    margin-top: 16px;
    font-family: "Lato", sans-serif; font-size: 20px; line-height: 1.35;
  }
  .rule { height: 1px; background: var(--grey-line); margin: 14px 56px 12px; }
  .address {
    font-family: "Lato", sans-serif; font-size: 20px; line-height: 1.35;
  }
  /* Back */
  .back__pattern {
    position: absolute; inset: 0;
    background: linear-gradient(160deg, var(--pattern-tone) 0%, var(--card-black) 80%);
  }
  .back__mark {
    position: absolute; left: 0; right: 0; top: 470px;
    font-family: "Lato", sans-serif; font-weight: 400;
    font-size: 52px; letter-spacing: 2px;
  }
  .back__cities {
    position: absolute; left: 0; right: 0; top: 570px;
    font-family: "Roboto Condensed", sans-serif; font-weight: 500;
    font-size: 20px; line-height: 1.25; letter-spacing: 0.5px;
  }
</style>
</head>
<body>
<main class="stage">
  <section class="card front" aria-label="Card front">
    <div class="front__mark">KMR</div>
    <div class="front__firm">Personal Injury<br>Attorneys</div>
    <div class="front__name">Tomas Velquist</div>
    <div class="divider">
      <span class="divider__rule"></span>
      <span class="divider__icon">
        <svg width="14" height="14" viewBox="0 0 14 14" aria-hidden="true"><rect x="4" y="1" width="6" height="12" rx="1.2" fill="none" stroke="#1e1f21" stroke-width="1.5"/></svg>
      </span>
      <span class="divider__icon">
        <svg width="14" height="14" viewBox="0 0 14 14" aria-hidden="true"><path d="M2 5c0-2 10-2 10 0v1H9V5H5v1H2z M3 7h8l1 5H2z" fill="#1e1f21"/></svg>
      </span>
      <span class="divider__icon">
        <svg width="14" height="14" viewBox="0 0 14 14" aria-hidden="true"><rect x="1.5" y="3" width="11" height="8" fill="none" stroke="#1e1f21" stroke-width="1.5"/><path d="M1.5 3l5.5 4.5L12.5 3" fill="none" stroke="#1e1f21" stroke-width="1.5"/></svg>
      </span>
      <span class="divider__rule"></span>
    </div>
    <div class="contact">
      (555)014-2736<br>(555)019-6521<br>Tomas@counselwestex.com
    </div>
    <div class="rule"></div>
    <div class="address">712 W. Harlow Ave. 4th Floor<br>Brookvale, CA 90000</div>
  </section>

  <section class="card back" aria-label="Card back">
    <div class="back__pattern" role="img" aria-label="Faint repeating firm-name pattern across the card"></div>
    <div class="back__mark">KMR</div>
    <div class="back__cities">LOS ANGELES - SANTA ANA<br>SAN DIEGO - SAN FRANCISCO</div>
  </section>
</main>
</body>
</html>
```